Birchway Inspection website (same layout, different look/style)

I want to create a NEW website based off the wordpress layout of another website. I want to have the same functionality/layout but a totally different look and style. I want my new website to have the same layout and features but to look totally different (different fonts, different logo, different colors, different style).

In the files section I have included different examples of the style I am looking for. That is conservative, trusted, simple, elegant and a little boring. I am trying to have the style of an insurnace company or bank website.

Please use that kind of style but use the same wordpress layout as the target website above.

Colors: blue, grey, green

You can use the same copy, I will add that later during the project.

My company is Birchway Inspections
birchwayinspections.example
tel:
(555) 318-7624
address:
4173 Fernhollow Rd,
Sarasota, FL 34000

Target Market(s)

Inspection

Industry/Entity Type

Inspection

Number of Pages Required

3 page

Font styles to use
Sans Serif

Colors
0054AA
0677BA
7BADD7
CADEEF
E8F1F8
0094D4
00A9DD
6FCCEA
C7EBF8
E9F6FB

Requirements
Must have
• Landing page, services page, about page

```html
<!DOCTYPE html>
<html lang="en">
<head>
<meta charset="utf-8">
<title>Birchway Inspections</title>
<link href="https://fonts.googleapis.com/css2?family=Archivo:ital,wght@0,400;0,600;0,700;0,800;1,800&family=Inter:wght@400;500;600&display=swap" rel="stylesheet">
<style>
:root{
  --navy:#0b2f57;
  --royal:#0054AA;
  --ocean:#0677BA;
  --sky:#0094D4;
  --bright:#00A9DD;
  --powder:#7BADD7;
  --aqua:#6FCCEA;
  --ice:#CADEEF;
  --frost:#E8F1F8;
  --haze:#E9F6FB;
  --text:#3d4f63;
  --white:#ffffff;
}
*{margin:0;padding:0;box-sizing:border-box}
html,body{width:1200px;height:3536px;overflow:hidden}
body{position:relative;background:var(--white);font-family:"Inter",sans-serif;color:var(--text)}
.abs{position:absolute}
h1,h2,h3,.head{font-family:"Archivo",sans-serif}

/* header */
.site-header{left:0;top:0;width:1200px;height:103px;background:rgba(0,84,170,.9);z-index:3}
.brand{left:114px;top:12px;color:var(--white);font-family:"Archivo",sans-serif;font-weight:800}
.brand-name{font-size:40px;letter-spacing:1px;line-height:1;display:flex;align-items:center;gap:10px}
.brand-name i{display:block;width:14px;height:14px;background:var(--white);border-radius:50%}
.brand-sub{font-size:12px;letter-spacing:2.6px;font-weight:800;margin-top:6px}
.brand-tag{font-size:7px;letter-spacing:5px;margin-top:4px;font-weight:800}
.topbar{left:700px;top:0;width:385px;height:38px;background:var(--ocean);border-radius:0 0 8px 8px;overflow:hidden;display:flex}
.topbar .phone{display:flex;align-items:center;gap:6px;padding-left:24px;width:185px;color:var(--white);font-size:15px;font-weight:500}
.topbar .req{flex:1;background:var(--bright);color:var(--white);font-size:12px;font-weight:700;display:flex;align-items:center;justify-content:center;letter-spacing:.3px}
.nav{top:64px;left:0;font-size:12.5px;font-weight:700;color:var(--white);font-family:"Archivo",sans-serif}
.nav span{position:absolute;white-space:nowrap}
.nav .active{border-bottom:2px solid var(--aqua);padding-bottom:6px}

/* hero */
.hero{left:0;top:0;width:1200px;height:751px;border-bottom-right-radius:230px;overflow:hidden;background:linear-gradient(180deg,#2f6aa8 0%,#4d86b9 40%,#2d5f8f 70%,#173f6d 100%)}
.hero::after{content:"";position:absolute;inset:0;background:linear-gradient(90deg,rgba(0,60,120,.55),rgba(0,60,120,.1))}
.hero-copy{left:120px;top:252px;color:var(--white);z-index:2}
.hero-copy h1{font-size:45px;font-weight:400;line-height:1.05;letter-spacing:.5px}
.hero-copy h1 b{display:block;font-weight:800;font-size:50px}
.hero-copy p{font-size:17px;line-height:1.35;margin-top:14px;width:430px}
.btn{display:inline-flex;align-items:center;justify-content:center;font-family:"Archivo",sans-serif;font-weight:700;letter-spacing:.4px;border-radius:6px}
.btn-hero{left:119px;top:437px;width:175px;height:42px;background:var(--bright);color:var(--white);font-size:15px;z-index:2}
.rating{left:127px;top:508px;color:var(--white);z-index:2}
.rating .row{display:flex;align-items:center;gap:14px;font-size:32px;font-family:"Archivo",sans-serif;font-weight:600}
.rating .stars{font-size:20px;letter-spacing:3px;color:var(--aqua)}
.rating small{display:block;font-size:10.5px;letter-spacing:.7px;margin-top:6px;font-weight:500}

.form-panel{left:695px;top:178px;width:400px;height:478px;background:rgba(255,255,255,.96);border-top:6px solid var(--sky);border-radius:12px;padding:34px 46px;z-index:2;color:var(--navy);box-shadow:0 12px 34px rgba(0,40,90,.25)}
.form-panel h2{font-size:27px;font-weight:800;line-height:1;color:var(--royal)}
.form-panel h2 span{display:block;font-weight:400;font-size:18px;margin-top:6px;color:var(--navy)}
.field{background:var(--frost);border:1px solid var(--ice);border-radius:5px;height:38px;margin-top:11px;display:flex;align-items:center;gap:10px;padding-left:15px;font-size:11px;color:#4a5a6b}
.field:first-of-type{margin-top:18px}
.field .dot{width:9px;height:9px;border-radius:50%;background:var(--powder)}
.field.msg{height:72px;align-items:flex-start;padding-top:14px}
.send{margin:14px 0 0 6px;width:294px;height:38px;background:var(--royal);font-size:13.5px;color:var(--white)}

/* section titles */
.section-title{width:1200px;text-align:center;font-size:36px;font-weight:400;color:var(--navy);letter-spacing:.5px}
.section-title b{font-weight:800;color:var(--royal)}
.section-title::after{content:"";display:block;width:68px;height:4px;background:var(--bright);margin:8px auto 0;border-radius:2px}

/* services */
.service-photo{top:897px;width:329px;height:236px;border-radius:10px 10px 0 0;background:linear-gradient(160deg,#8fc3e6 0%,#c7d7e3 55%,#7b6a5c 100%)}
.card{top:1089px;width:290px;height:190px;background:var(--white);border-radius:10px;border-bottom:4px solid var(--bright);box-shadow:0 8px 26px rgba(0,50,110,.14);text-align:center;padding-top:45px}
.card.dark{background:var(--royal);color:var(--white)}
.card h3{font-size:18px;font-weight:700;color:var(--royal);letter-spacing:.3px}
.card.dark h3{color:var(--white)}
.card p{font-size:10.5px;line-height:1.6;margin:8px auto 0;width:230px}
.card .btn{width:152px;height:35px;margin-top:16px;font-size:12px;background:var(--royal);color:var(--white)}
.card.dark .btn{background:var(--bright)}
.icon-disc{top:1056px;width:66px;height:66px;border-radius:50%;background:var(--sky);border:3px solid var(--white);display:flex;align-items:center;justify-content:center}

/* about band */
.divider{left:622px;top:1350px;width:2px;height:64px;background:var(--royal)}
.about{left:0;top:1383px;width:1200px;height:587px;background:var(--ocean);border-radius:200px 0 220px 0;overflow:hidden}
.about-photo{left:0;top:0;width:780px;height:587px;background:linear-gradient(100deg,#5a4e48 0%,#5f7e9c 45%,rgba(6,119,186,0) 100%)}
.about-copy{left:620px;top:1487px;width:490px;color:var(--white)}
.about-copy h2{font-size:36px;font-weight:400;line-height:1.1;letter-spacing:.5px}
.about-copy h2 b{display:block;font-weight:800}
.about-copy h2::after{content:"";display:block;width:70px;height:3px;background:var(--aqua);margin:10px 0 0 4px}
.about-copy h3{font-size:19px;font-weight:800;line-height:1.55;margin:14px 0 0 5px}
.about-copy p{font-size:15px;line-height:1.6;margin:26px 0 0 5px;color:var(--haze)}
.btn-about{left:625px;top:1815px;width:179px;height:44px;background:var(--white);color:var(--royal);font-size:14px}

/* reviews */
.contact-zone{left:0;top:2300px;width:1200px;height:1000px;background:linear-gradient(160deg,#0677BA 0%,#0054AA 60%,#0a3f80 100%)}
.reviews{left:0;top:1970px;width:1200px;height:577px;background:var(--white);border-bottom-right-radius:240px}
.subtitle{left:0;top:2112px;width:1200px;text-align:center;font-size:17px;color:var(--navy)}
.frame-tl{left:259px;top:2175px;width:108px;height:100px;border-left:9px solid var(--aqua);border-top:9px solid var(--aqua);border-top-left-radius:10px}
.frame-br{left:812px;top:2350px;width:107px;height:98px;border-right:9px solid var(--aqua);border-bottom:9px solid var(--aqua);border-bottom-right-radius:10px}
.review-card{left:268px;top:2183px;width:643px;height:257px;background:var(--haze);border:1.5px solid var(--ice);border-radius:8px;text-align:center;padding:50px 70px 0}
.review-card p{font-size:15px;line-height:1.8;color:var(--text)}
.review-card .stars{color:var(--sky);font-size:19px;letter-spacing:2px;margin-top:8px}
.review-card .who{font-family:"Archivo",sans-serif;font-weight:700;color:var(--royal);font-size:17px;margin-top:4px}
.quote{left:557px;top:2156px;width:62px;height:62px;border-radius:50%;background:var(--royal);display:flex;align-items:center;justify-content:center;color:var(--white);font-family:"Archivo",sans-serif;font-size:48px;font-weight:800;line-height:1;padding-top:18px}
.arrow{top:2276px}

/* contact */
.contact-copy{left:137px;top:2684px;color:var(--white)}
.contact-copy h2{font-size:29px;font-weight:400;letter-spacing:.5px}
.expert{left:122px;top:2731px;width:448px;height:56px;background:var(--white);border-radius:8px;display:flex;align-items:center;padding-left:28px;font-family:"Archivo",sans-serif;font-weight:800;font-size:35px;color:var(--royal);letter-spacing:.5px}
.contact-text{left:132px;top:2803px;width:420px;color:var(--white);font-size:15px;line-height:1.75}
.btn-contact{left:137px;top:2928px;width:228px;height:47px;background:var(--bright);color:var(--white);font-size:14px}
.city{left:600px;top:2664px;width:494px;height:316px;border-radius:60px 0 60px 0;background:linear-gradient(180deg,#bfe3f4 0%,#7fb7dc 40%,#5b8ca5 75%,#3e6f8a 100%);opacity:.9}

/* footer */
.footer{left:0;top:3135px;width:1200px;height:401px;background:var(--frost);border-top-left-radius:190px}
.foot-brand{left:134px;top:3222px;color:var(--royal);font-family:"Archivo",sans-serif;font-weight:800;text-align:center}
.foot-brand .name{font-size:46px;line-height:1;display:flex;align-items:center;gap:10px}
.foot-brand .name i{display:block;width:16px;height:16px;border-radius:50%;background:var(--royal)}
.foot-brand .sub{font-size:13.5px;letter-spacing:2.6px;margin-top:8px}
.foot-brand .tag{font-size:7px;letter-spacing:5px;margin-top:8px}
.socials{left:203px;top:3336px;display:flex;gap:6px}
.socials i{width:26px;height:26px;border-radius:50%;background:var(--ocean);display:block}
.foot-col{top:3220px}
.foot-col h4{font-family:"Archivo",sans-serif;font-size:17px;font-weight:700;color:var(--royal);border-left:3px solid var(--bright);padding-left:10px;line-height:1}
.foot-col ul{list-style:none;margin:14px 0 0 14px}
.foot-col li{font-size:13.5px;color:var(--navy);line-height:29px}
.contact-line{display:flex;align-items:center;gap:10px;font-size:12.5px;color:var(--navy);margin:12px 0 0 14px;white-space:nowrap}
.contact-line + .contact-line{margin-top:11px}
.ci{width:22px;height:22px;border-radius:50%;background:var(--ocean);display:flex;align-items:center;justify-content:center;flex:none}
.map{left:895px;top:3251px;width:207px;height:154px;border-radius:8px;background:linear-gradient(135deg,var(--haze),var(--ice))}
.foot-rule{left:0;top:3467px;width:1200px;height:1px;background:var(--powder)}
.copyright{left:0;top:3490px;width:1200px;text-align:center;font-size:12px;color:var(--text)}
.copyright u{color:var(--royal)}
</style>
</head>
<body>

<div class="abs hero" role="img" aria-label="Photo of a father holding his child, pointing at the roof of a family home"></div>

<header class="abs site-header">
  <div class="abs brand">
    <div class="brand-name"><i></i>BIRCHWAY</div>
    <div class="brand-sub">INSPECTIONS</div>
    <div class="brand-tag">LICENSED INSPECTORS</div>
  </div>
  <div class="abs topbar">
    <div class="phone">
      <svg width="17" height="17" viewBox="0 0 24 24"><circle cx="12" cy="12" r="12" fill="#fff"/><path d="M8.2 6.5l2 2.3-1.1 1.6c.8 1.7 2 2.9 3.6 3.7l1.6-1.1 2.3 2-1.2 1.8c-4.3-.5-8.2-4.4-8.7-8.7z" fill="#0677BA"/></svg>
      (555) 318-7624
    </div>
    <div class="req">REQUEST INSPECTION</div>
  </div>
  <nav class="abs nav">
    <span class="active" style="left:470px">HOME</span>
    <span style="left:563px">ABOUT US</span>
    <span style="left:678px">INSPECTION SERVICES</span>
    <span style="left:876px">REVIEWS</span>
    <span style="left:983px">PAY ONLINE</span>
  </nav>
</header>

<div class="abs hero-copy">
  <h1>BIRCHWAY INSURANCE <b>INSPECTIONS</b></h1>
  <p>Florida's Most Trusted Residential &amp; Commercial Insurance Inspection Specialists</p>
</div>
<a class="abs btn btn-hero">CONTACT US</a>
<div class="abs rating">
  <div class="row">Revuline <span class="stars">★★★★★</span></div>
  <small>HUNDREDS OF SATISFIED CUSTOMERS</small>
</div>

<form class="abs form-panel">
  <h2>GET STARTED TODAY <span>WITH BIRCHWAY INSPECTIONS</span></h2>
  <div class="field"><span class="dot"></span>I am</div>
  <div class="field"><span class="dot"></span>Email address</div>
  <div class="field"><span class="dot"></span>Full Name</div>
  <div class="field"><span class="dot"></span>Phone</div>
  <div class="field msg"><span class="dot"></span>Message</div>
  <div class="btn send">SEND MESSAGE</div>
</form>

<h2 class="abs section-title" style="top:804px">OUR <b>SERVICES</b></h2>

<div class="abs service-photo" style="left:88px" role="img" aria-label="Inspector measuring a roof edge with a tape measure"></div>
<div class="abs service-photo" style="left:430px;background:linear-gradient(160deg,#d5dde3 0%,#9fb1bf 50%,#4b6478 100%)" role="img" aria-label="Inspector in a hard hat examining roof shingles"></div>
<div class="abs service-photo" style="left:773px;background:linear-gradient(170deg,#8fbbe0 0%,#c9dbe8 40%,#3b4a57 100%)" role="img" aria-label="Dark tiled roof of a modern house against a blue sky"></div>

<div class="abs card" style="left:110px">
  <h3>WIND MITIGATION</h3>
  <p>Lorem ipsum dolor sit amet, consectetur adipiscing elit, sed do eiusmod tempor</p>
  <div class="btn">LEARN MORE</div>
</div>
<div class="abs card dark" style="left:453px">
  <h3>FOUR POINT INSPECTION</h3>
  <p>Lorem ipsum dolor sit amet, consectetur adipiscing elit, sed do eiusmod tempor</p>
  <div class="btn">LEARN MORE</div>
</div>
<div class="abs card" style="left:796px">
  <h3>ROOF CERTIFICATION</h3>
  <p>Lorem ipsum dolor sit amet, consectetur adipiscing elit, sed do eiusmod tempor</p>
  <div class="btn">LEARN MORE</div>
</div>

<div class="abs icon-disc" style="left:220px">
  <svg width="36" height="24" viewBox="0 0 36 24" fill="none" stroke="#fff" stroke-width="2" stroke-linecap="round"><path d="M2 8h20a4 4 0 1 0-4-4"/><path d="M2 14h28a4 4 0 1 1-4 4"/><path d="M8 20h8"/></svg>
</div>
<div class="abs icon-disc" style="left:564px">
  <svg width="32" height="32" viewBox="0 0 32 32" fill="none" stroke="#fff" stroke-width="2.2" stroke-linecap="round"><circle cx="13" cy="13" r="9"/><path d="M20 20l9 9"/></svg>
</div>
<div class="abs icon-disc" style="left:909px">
  <svg width="30" height="34" viewBox="0 0 30 34" fill="none" stroke="#fff" stroke-width="2" stroke-linecap="round" stroke-linejoin="round"><circle cx="15" cy="13" r="10"/><path d="M10 13l3.5 3.5L20 10"/><path d="M9 21l-3 11 5-3 3 4M21 21l3 11-5-3-3 4"/></svg>
</div>

<div class="abs divider"></div>
<section class="abs about">
  <div class="abs about-photo" role="img" aria-label="Close view of a tiled roof with chimney and skylights"></div>
</section>
<div class="abs about-copy">
  <h2>BIRCHWAY INSURANCE <b>INSPECTIONS</b></h2>
  <h3>Florida Wind Mitigation, Four Point, &amp; Roof Certification Insurance Inspections</h3>
  <p>Lorem ipsum dolor sit amet, consectetur adipiscing elit, sed do eiusmod tempor incididunt ut labore et dolore magna aliqua. Ut enim ad minim veniam, quis nostrud exercitation ullamco laboris nisi ut aliquip ex ea commodo consequat. Duis aute irure dolor in reprehenderit in voluptate velit esse</p>
</div>
<a class="abs btn btn-about">LEARN MORE</a>

<div class="abs contact-zone" role="img" aria-label="Aerial view of a coastal city under a blue overlay"></div>

<section class="abs reviews"></section>
<h2 class="abs section-title" style="top:2026px">CUSTOMER <b>REVIEWS</b></h2>
<p class="abs subtitle">Reviews from our amazing customers</p>
<div class="abs frame-tl"></div>
<div class="abs frame-br"></div>
<div class="abs review-card">
  <p>Lorem ipsum dolor sit amet, consectetur adipiscing elit, sed do eiusmod tempor incididunt ut labore et dolore magna aliqua. Ut enim ad minim veniam, quis nostrud exercitation ullamco laboris nisi ut aliquip ex ea commodo consequat</p>
  <div class="stars">★★★★★</div>
  <div class="who">Dana Whitfield</div>
</div>
<div class="abs quote">“</div>
<svg class="abs arrow" style="left:174px" width="26" height="46" viewBox="0 0 26 46" fill="none" stroke="#0677BA" stroke-width="2"><path d="M24 2L3 23l21 21"/></svg>
<svg class="abs arrow" style="left:1000px" width="26" height="46" viewBox="0 0 26 46" fill="none" stroke="#0677BA" stroke-width="2"><path d="M2 2l21 21L2 44"/></svg>

<div class="abs contact-copy"><h2>CONTACT US TODAY</h2></div>
<div class="abs expert">INSURANCE EXPERT</div>
<p class="abs contact-text">Lorem ipsum dolor sit amet, consectetur adipiscing elit, sed do eiusmod tempor incididunt ut labore et dolore magna aliqua. Ut enim ad minim veniam, quis nostrud exercitation ullamco laboris nisi</p>
<a class="abs btn btn-contact">REQUEST INSPECTION</a>
<div class="abs city" role="img" aria-label="Bright aerial photo of city towers and neighbourhood rooftops"></div>

<footer class="abs footer"></footer>
<div class="abs foot-brand">
  <div class="name"><i></i>BIRCHWAY</div>
  <div class="sub">INSPECTIONS</div>
  <div class="tag">LICENSED INSPECTORS</div>
</div>
<div class="abs socials"><i></i><i></i><i></i></div>

<div class="abs foot-col" style="left:432px">
  <h4>QUICK LINKS</h4>
  <ul>
    <li>Request Inspection</li>
    <li>Our Services</li>
    <li>About Us</li>
    <li>Contact Us</li>
    <li>Client Login</li>
  </ul>
</div>
<div class="abs foot-col" style="left:600px">
  <h4>CONTACT US</h4>
  <div class="contact-line"><span class="ci"><svg width="12" height="12" viewBox="0 0 24 24"><path d="M5 2l4 4.5-2.2 3c1.6 3.3 3.9 5.6 7.2 7.2l3-2.2L22 19l-2.4 3.5C11 21.5 2.5 13 1.5 4.4z" fill="#fff"/></svg></span>(555) 318-7624</div>
  <div class="contact-line"><span class="ci"><svg width="12" height="10" viewBox="0 0 24 18" fill="none" stroke="#fff" stroke-width="2.4"><rect x="1.5" y="1.5" width="21" height="15"/><path d="M2 2l10 8 10-8"/></svg></span>info@birchwayinspections.example</div>
</div>
<div class="abs foot-col" style="left:895px">
  <h4>LOCATION</h4>
</div>
<div class="abs map" role="img" aria-label="Street map showing 4173 Fernhollow Rd, Sarasota, FL 34000">
  <svg class="abs" style="left:93px;top:32px" width="22" height="30" viewBox="0 0 22 30"><path d="M11 29C11 29 1 17 1 11a10 10 0 0 1 20 0c0 6-10 18-10 18z" fill="#0054AA"/><circle cx="11" cy="11" r="4" fill="#fff"/></svg>
</div>
<div class="abs foot-rule"></div>
<p class="abs copyright">© 2024 <u>Birchway Inspections</u>. All Rights Reserved</p>

</body>
</html>
```